Tech business card design

We need an amazing business card design for our new business 'Vantry' a marketing tech startup based in Sydney, Australia. We provide an online marketplace for businesses to search and buy advertising media, connect with service providers and learn more about marketing. We wish to communicate 'cool tech', reliability and professionalism and design based around our logo.

Target Market(s)

Business Owners

Contact Information for Business Card

Name
Position
Email Address
Website
Phone Number

Font styles to use
Other font styles liked:
• Avenir & Avenir Next

Colors

Designer to choose colors to be used in the design.

```html
<!DOCTYPE html>
<html lang="en">
<head>
<meta charset="utf-8">
<title>Vantry – Business Card</title>
<link href="https://fonts.googleapis.com/css2?family=Nunito+Sans:wght@300;400;600;900&display=swap" rel="stylesheet">
<style>
  :root {
    --stage: #2a2c31;
    --navy: #1c1b4a;
    --navy-light: #2c2b62;
    --ink: #1e1d4d;
    --text: #2b2b33;
    --muted: #55557a;
    --white: #ffffff;
    --url-on-navy: #b9b8d9;
  }
  * { box-sizing: border-box; margin: 0; padding: 0; }
  html, body {
    width: 1200px; height: 900px; overflow: hidden;
    background: var(--stage);
    font-family: "Nunito Sans", "Avenir Next", Avenir, sans-serif;
  }
  .canvas { position: relative; width: 1200px; height: 900px; }

  .card {
    position: absolute;
    border-radius: 26px;
    overflow: hidden;
    box-shadow: 0 18px 40px rgba(0,0,0,.45);
  }

  /* Front */
  .card-front {
    left: 110px; top: 180px; width: 340px; height: 540px;
    background: var(--white);
  }
  .wordmark {
    font-weight: 900;
    letter-spacing: -2px;
    line-height: 1;
  }
  .card-front .wordmark {
    position: absolute; left: 38px; top: 60px;
    font-size: 82px; color: var(--ink);
  }
  .contact {
    position: absolute; left: 110px; top: 300px; right: 20px;
    color: var(--text);
  }
  .identity {
    border-left: 2px solid var(--ink);
    padding-left: 10px;
    margin-bottom: 22px;
  }
  .identity .name { font-size: 21px; font-weight: 400; letter-spacing: .5px; color: var(--ink); }
  .identity .role { font-size: 15px; font-weight: 400; color: var(--muted); }
  .contact-list { list-style: none; }
  .contact-list li {
    display: flex; align-items: center; gap: 10px;
    font-size: 15px; margin-bottom: 10px; white-space: nowrap;
  }
  .contact-list svg { width: 14px; height: 14px; flex: none; }

  /* Back */
  .card-back {
    left: 540px; top: 280px; width: 560px; height: 340px;
    background: var(--navy);
  }
  .card-back .band { position: absolute; inset: 0; }
  .card-back .wordmark {
    position: absolute; left: 0; right: 0; top: 78px;
    text-align: center; font-size: 110px; color: var(--white);
  }
  .card-back .url {
    position: absolute; left: 0; right: 0; top: 228px;
    text-align: center; font-size: 14px; font-weight: 300;
    letter-spacing: 4px; color: var(--url-on-navy);
  }
</style>
</head>
<body>
<main class="canvas">

  <section class="card card-front" aria-label="Business card front">
    <div class="wordmark">vantry</div>
    <div class="contact">
      <div class="identity">
        <p class="name">DANIEL ROWE</p>
        <p class="role">Founder, Director</p>
      </div>
      <ul class="contact-list">
        <li>
          <svg viewBox="0 0 14 14" aria-hidden="true"><rect x="3.5" y="1" width="7" height="12" rx="1.2" fill="none" stroke="#1e1d4d" stroke-width="1.2"/><circle cx="7" cy="11" r=".7" fill="#1e1d4d"/></svg>
          +61 (0)412 555 208
        </li>
        <li>
          <svg viewBox="0 0 14 14" aria-hidden="true"><rect x="1" y="3" width="12" height="8" fill="#1e1d4d"/><path d="M1 3 L7 8 L13 3" fill="none" stroke="#fff" stroke-width="1"/></svg>
          daniel@vantrymedia.com.au
        </li>
        <li>
          <svg viewBox="0 0 14 14" aria-hidden="true"><circle cx="7" cy="7" r="6" fill="#1e1d4d"/><path d="M1 7 H13 M7 1 C4 4 4 10 7 13 M7 1 C10 4 10 10 7 13" fill="none" stroke="#fff" stroke-width=".8"/></svg>
          www.vantrymedia.com.au
        </li>
      </ul>
    </div>
  </section>

  <section class="card card-back" aria-label="Business card back">
    <svg class="band" viewBox="0 0 560 340" preserveAspectRatio="none" aria-hidden="true">
      <path d="M0 150 Q280 260 560 150 L560 340 L0 340 Z" fill="var(--navy-light)" opacity=".75"/>
      <path d="M0 150 Q280 260 560 150" fill="none" stroke="#3d3c7a" stroke-width="1.5"/>
    </svg>
    <div class="wordmark">vantry</div>
    <p class="url">www.vantrymedia.com.au</p>
  </section>

</main>
</body>
</html>
```